Web site for Tree Removal Company

What we are looking for:
-------------------------------
Looking for a wordpress web site, you can provide your own template or we can supply you with one (http://quorvel.plindatheme.net).

What we do
---------------
To see what we do please go to google Australia and google "Tree removal Sydney" or "Tree Removal Melbourne".

Web site requirements
-----------------------------
We prefer you to use our template as it has all our requirements in already.
- Responsive.
- Based on Wordpress.
- Full complaint and compatible with plugs.

Look, Feel and Appearance
------------------------------------
Please use the logo (see attached), for colour scheme, look and feel of the web site.

Thank you for your time and effort!

Target Market(s)

Tree Removal for Residential Homes

Industry/Entity Type

It Company

Number of Pages Required

4 page

Font styles to use
Serif
Sans Serif

Requirements
Must have
• Wordpress
Nice to have
• Original artwork, images and text
Should not have
• non related images or wording

```html
<!DOCTYPE html>
<html lang="en">
<head>
<meta charset="utf-8">
<title>Arbor Kin – Tree Removal</title>
<link rel="stylesheet" href="https://fonts.googleapis.com/css2?family=Fira+Sans:ital,wght@0,400;0,500;0,600;1,600&family=Open+Sans:wght@400;600&family=Arimo&display=swap">
<style>
:root{
  --dark:#232323;
  --darker:#141414;
  --black:#000;
  --mint:#7fdba2;
  --mint-text:#86e0a8;
  --white:#fff;
  --grey:#a9a9a9;
  --ink:#1d1d1d;
}
*{box-sizing:border-box;margin:0;padding:0}
html,body{width:1200px;height:2230px;overflow:hidden}
body{position:relative;background:var(--dark);font-family:"Open Sans",sans-serif;color:var(--white)}
.abs{position:absolute}

/* header */
.site-header{left:0;top:0;width:1200px;height:155px;background:var(--dark)}
.brand{left:108px;top:28px;display:flex;flex-direction:column;align-items:center;gap:10px}
.brand-dot{width:78px;height:78px;border-radius:50%;background:#5fbf8c}
.brand-name{font-family:"Fira Sans",sans-serif;font-size:22px;letter-spacing:3px;color:#bdbdbd;font-weight:500}
.consult{right:100px;top:4px;text-align:right;font-family:"Fira Sans",sans-serif}
.consult-label{color:var(--mint-text);font-size:22px}
.consult-phone{color:var(--white);font-size:28px;margin-top:4px}
.social{right:100px;top:112px;display:flex;gap:7px}
.social span{width:27px;height:27px;border-radius:50%;background:#bdbdbd}

/* nav */
.main-nav{left:0;top:155px;width:1200px;height:50px;background:var(--darker);border-top:1px solid var(--mint)}
.main-nav ul{list-style:none;position:relative;height:100%}
.main-nav li{position:absolute;top:0;height:49px;line-height:49px;transform:translateX(-50%);font-family:Arimo,sans-serif;font-size:14px;color:var(--white)}
.nav-sep{top:6px;width:1px;height:38px;background:#2e2e2e}

/* hero */
.hero-bg{left:0;top:205px}
.hero-frame{left:101px;top:223px;width:999px;height:433px;border:4px solid var(--white);overflow:hidden}
.hero-photo{width:100%;height:100%;background:linear-gradient(135deg,#3c4a3a 0%,#7a8b8c 45%,#c9d4da 62%,#3b3f45 100%)}
.hero-caption{left:0;bottom:0;width:100%;height:52px;background:rgba(30,30,30,.85);text-align:center;font-family:"Fira Sans",sans-serif;font-size:31px;line-height:50px}
.hero-caption em{font-style:normal;color:var(--mint-text);font-weight:600}

/* intro columns */
.intro-col{top:692px;width:303px}
.intro-col h2{font-family:"Fira Sans",sans-serif;font-weight:400;font-size:24px;height:43px}
.intro-photo{height:117px;border:3px solid var(--white)}
.intro-col p{margin-top:17px;font-size:12.5px;line-height:20px;font-weight:600}

/* services */
.services{left:0;top:1028px;width:1200px;height:452px;background:var(--mint)}
.service{width:290px;text-align:center}
.service-photo{height:126px;border:3px solid var(--white)}
.service-name{margin-top:8px;font-family:"Fira Sans",sans-serif;font-size:20px;color:var(--ink);letter-spacing:.5px}

/* testimonial */
.testimonial-photo{left:104px;top:1544px;width:352px;height:242px;background:linear-gradient(180deg,#dfe3e6 0%,#c7a36a 45%,#9c7a45 75%,#8d8778 100%)}
.quote-title{left:477px;top:1546px;width:620px;font-family:"Fira Sans",sans-serif;font-size:25px;line-height:32px}
.quote-body{left:487px;top:1620px;width:605px;font-size:13px;line-height:22px}
.quote-sign{right:115px;top:1776px;text-align:right;font-family:"Fira Sans",sans-serif;font-style:italic;font-weight:600;font-size:14px;line-height:20px;color:var(--mint-text)}

/* footer */
.site-footer{left:0;top:1860px;width:1200px;height:370px;background:var(--black)}
.footer-title{left:101px;top:17px;width:999px;height:48px;background:var(--mint);color:var(--ink);text-align:center;font-family:"Fira Sans",sans-serif;font-weight:500;font-size:21px;line-height:48px;letter-spacing:.5px}
.service-list{list-style:none;top:95px;font-family:Arimo,sans-serif;font-size:14px}
.service-list li{height:26px;line-height:26px;padding-left:20px;position:relative}
.service-list li::before{content:"";position:absolute;left:0;top:12px;width:9px;height:2px;background:var(--mint)}
.service-list li::after{content:"";position:absolute;left:5px;top:9px;width:5px;height:5px;border-top:2px solid var(--mint);border-right:2px solid var(--mint);transform:rotate(45deg)}
.copyright{left:107px;top:320px;font-family:Arimo,sans-serif;font-size:14px}
.legal{right:100px;top:320px;font-family:Arimo,sans-serif;font-size:14px;word-spacing:2px}
</style>
</head>
<body>

<header class="site-header abs">
  <div class="brand abs">
    <span class="brand-dot"></span>
    <span class="brand-name">ARBOR KIN</span>
  </div>
  <div class="consult abs">
    <div class="consult-label">Request &nbsp;Free Consultation :</div>
    <div class="consult-phone">123-555-0186</div>
  </div>
  <div class="social abs" aria-label="Social links"><span></span><span></span><span></span><span></span><span></span><span></span></div>
</header>

<nav class="main-nav abs">
  <ul>
    <li style="left:163px">HOME</li>
    <li style="left:306px">ABOUT</li>
    <li style="left:476px">WHAT WE DO</li>
    <li style="left:657px">COUPONS</li>
    <li style="left:827px">THE BUZZ</li>
    <li style="left:1003px">CONTACT US</li>
  </ul>
  <span class="nav-sep abs" style="left:229px"></span>
  <span class="nav-sep abs" style="left:381px"></span>
  <span class="nav-sep abs" style="left:570px"></span>
  <span class="nav-sep abs" style="left:745px"></span>
  <span class="nav-sep abs" style="left:910px"></span>
</nav>

<svg class="hero-bg abs" width="1200" height="500" viewBox="0 0 1200 500" aria-hidden="true">
  <path d="M0 0H1200V320Q1150 328 1100 332V345L0 345Z" fill="#7fdba2"/>
  <path d="M0 345L101 328V345Z" fill="#232323"/>
  <path d="M1100 332Q1150 326 1200 318V500H1100Z" fill="#232323"/>
</svg>

<section class="hero-frame abs">
  <div class="hero-photo" role="img" aria-label="Arborist in a red helmet cutting a log with a chainsaw, wood chips spraying"></div>
  <div class="hero-caption abs">Award Winning Tree Removal <em>Company in U.S.A</em></div>
</section>

<section class="intro-col abs" style="left:101px">
  <h2>Why Arbor Kin</h2>
  <div class="intro-photo" role="img" aria-label="Chainsaw cutting a felled trunk in the forest" style="background:linear-gradient(135deg,#6f8f3a,#c9b36a 55%,#3d3a2c)"></div>
  <p>Lorem Ipsum is simply dummy text of the printing and typesetting industry. Lorem Ipsum has been the industry's standard dummy text ever since the 1500s, when an unknown printer took a galley of type and scrambled it to make a type specimen book has survived.</p>
</section>
<section class="intro-col abs" style="left:449px">
  <h2>See Where We’ve Worked</h2>
  <div class="intro-photo" role="img" aria-label="Climber working high in a leafy tree canopy" style="background:linear-gradient(135deg,#9ccd3c,#5e8b22 50%,#c3e36a)"></div>
  <p>Lorem Ipsum is simply dummy text of the printing and typesetting industry. Lorem Ipsum has been the industry's standard dummy text ever since the 1500s, when an unknown printer took a galley of type and scrambled it to make a type specimen book has survived.</p>
</section>
<section class="intro-col abs" style="left:797px">
  <h2>Community</h2>
  <div class="intro-photo" role="img" aria-label="Worker mowing a green lawn in front of hedges" style="background:linear-gradient(180deg,#2f3d2a,#4d7a2e 45%,#7fbf3c)"></div>
  <p>Lorem Ipsum is simply dummy text of the printing and typesetting industry. Lorem Ipsum has been the industry's standard dummy text ever since the 1500s, when an unknown printer took a galley of type and scrambled it to make a type specimen book has survived.</p>
</section>

<section class="services abs">
  <div class="service abs" style="left:123px;top:50px"><div class="service-photo" role="img" aria-label="Chainsaw cutting a felled trunk" style="background:linear-gradient(135deg,#6f8f3a,#c9b36a 55%,#3d3a2c)"></div><div class="service-name">Tree Removal</div></div>
  <div class="service abs" style="left:462px;top:50px"><div class="service-photo" role="img" aria-label="Climber trimming branches in a tree" style="background:linear-gradient(135deg,#9ccd3c,#5e8b22 50%,#c3e36a)"></div><div class="service-name">Tree Trimming</div></div>
  <div class="service abs" style="left:784px;top:50px"><div class="service-photo" role="img" aria-label="Worker with a grinder on a lawn" style="background:linear-gradient(180deg,#2f3d2a,#4d7a2e 45%,#7fbf3c)"></div><div class="service-name">Stump Grinding</div></div>
  <div class="service abs" style="left:122px;top:258px"><div class="service-photo" role="img" aria-label="Large house behind a tall tree after a storm" style="background:linear-gradient(180deg,#e8eef2,#7d8a78 55%,#5d7a3a)"></div><div class="service-name">Storm Damage</div></div>
  <div class="service abs" style="left:460px;top:258px"><div class="service-photo" role="img" aria-label="Crew standing in front of a timber house frame" style="background:linear-gradient(180deg,#dfe3e6,#c7a36a 45%,#9c7a45 80%)"></div><div class="service-name">Tree Cabling</div></div>
  <div class="service abs" style="left:782px;top:258px"><div class="service-photo" role="img" aria-label="Arborist with ropes working at the base of a tree" style="background:linear-gradient(135deg,#7a5d4a,#5d8a3a 50%,#2f4a22)"></div><div class="service-name">75’ Bucket Truck</div></div>
</section>

<div class="testimonial-photo abs" role="img" aria-label="Five workers standing before a timber house frame with yellow edge rails"></div>
<h2 class="quote-title abs">"I would recommend Arbor Kin. to any<br>&nbsp;prospective purchaser"</h2>
<p class="quote-body abs">"Marren Homes Ltd. has used the services of Dane Orwell and his Ridge Guard. I was impressed both with the quality of the Ridge Guard Dane Supplied and his knowledge and understanding of the new requirements being enforced by the Labour Dept. I had a meeting with the Labour Dept. representative in my office which Dane attended and Dane introduced a simple and easy way to address the issue which was more than the Labour Dept. were prepared to offer. I would recommend Ridge Guard Ltd. to any prospective purchaser."</p>
<div class="quote-sign abs">Clara Voss.<br>Director of Marren Homes Ltd</div>

<footer class="site-footer abs">
  <h2 class="footer-title abs">COMPREHENSIVE SERVICES OFFERED BY ARBOR KIN</h2>
  <ul class="service-list abs" style="left:119px">
    <li>Certified Arborist</li><li>Bucket &nbsp;Service</li><li>Crane Service</li><li>Deadwooding</li><li>Xl Tree Removal</li><li>Ash Borer Control</li><li>Pruning</li>
  </ul>
  <ul class="service-list abs" style="left:375px">
    <li>Stump Grinding</li><li>Root Collar Excavation</li><li>Licensed Pest Control</li><li>Vertical Mulching</li><li>Tree Inventories</li><li>Chipping Service</li><li>Tree Selection Service</li>
  </ul>
  <ul class="service-list abs" style="left:648px;top:97px">
    <li>Tree/shrub Fertilization</li><li>Spraying</li><li>Lightning Protection</li><li>Cable Bracing</li><li>Disease Control</li><li>Expert Climbers</li><li>Disease Control</li>
  </ul>
  <ul class="service-list abs" style="left:914px">
    <li>Commercial Service</li><li>Tree Shaping</li><li>Crown Reduction</li><li>Planting</li><li>Pre-construction</li><li>Tree Preservation</li><li>Consulting</li>
  </ul>
  <div class="copyright abs">Copyright 2010 © Fenlow Arbor Kin Inc. All Right Reserved.</div>
  <div class="legal abs">Privacy Policy &nbsp;&nbsp;| &nbsp;&nbsp;Terms and Conditions</div>
</footer>

</body>
</html>
```